New Wrestling company needs a website

We need a website design for a new wrestling company in Australia that will be running 3-4 events per year. Wrestling company is Coral Tide Grappling (CTG).

The design of the logo is in place and can be provided, and I have purchased the website domain.

A detailed description of the intent and purpose of this company can be provided.

The aim would be to have around 5 specific pages on CTG, with two standard “about” and “contact” pages. E.g.
- About CTG (focus and purpose of the company)
- CTG Events (specific focus on events run by CTG)
- CTG News (news and stories on wrestling’s across Oceania)
- CTG Media (where to watch CTG and our partners))
- CTG Partners and Sponsors (partner and affiliate information)
- CTG Power Rankings (top 10 ranked wrestlers from Oceania which is updated weekly)
- CTG fans (highlighting how to become part of CTG as a fan)
- Contact CTG
Updates

The logo design should now be included in the brief, please feel free to reach out to me directly if you can't access it or require any other information.

Target Market(s)

Wrestling Fans

Industry/Entity Type

Sport / Wrestling

Coding

Coded - Design and coding required

Number of Pages Required

5+ page

Requirements
Must have
• A Wrestling and or Sports feel to the website design

```html
<!DOCTYPE html>
<html lang="en">
<head>
<meta charset="utf-8">
<title>Coral Tide Grappling</title>
<link href="https://fonts.googleapis.com/css2?family=Audiowide&family=Rajdhani:wght@500;600;700&family=Arimo:wght@400;700&display=swap" rel="stylesheet">
<style>
:root{
  --bg:#050505;
  --bg-alt:#0b0d12;
  --footer:#0a0b0e;
  --blue:#2a9de0;
  --blue-band:#2f9ee1;
  --white:#ffffff;
  --line:#2a2d33;
}
*{margin:0;padding:0;box-sizing:border-box}
html,body{width:1200px;height:4261px;overflow:hidden;background:var(--bg);color:var(--white)}
body{position:relative;font-family:"Arimo",Arial,sans-serif}
.abs{position:absolute}
.display{font-family:"Audiowide",sans-serif;letter-spacing:1px}
.photo{position:absolute}

/* header */
.site-header{position:absolute;left:0;top:0;width:1200px;height:139px;background:#000}
.brand{position:absolute;left:112px;top:38px;display:flex;align-items:center;gap:10px}
.brand-dot{width:22px;height:22px;border-radius:50%;background:var(--blue)}
.brand-name{font-family:"Audiowide",sans-serif;font-size:44px;color:var(--blue);line-height:1}
.contact-item{position:absolute;top:25px;display:flex;align-items:center;gap:14px}
.contact-icon{width:40px;height:40px;border:1.5px solid var(--blue);border-radius:50%;display:flex;align-items:center;justify-content:center}
.contact-label{font-family:"Rajdhani",sans-serif;font-size:13px;color:#aab;font-weight:500}
.contact-value{font-family:"Rajdhani",sans-serif;font-size:16px;color:var(--white);font-weight:500;margin-top:2px}
.main-nav{position:absolute;left:364px;top:94px;display:flex;gap:27px;font-family:"Rajdhani",sans-serif;font-weight:700;font-size:13px;letter-spacing:.3px}
.main-nav a{color:var(--white);text-decoration:none}
.main-nav a.active{color:var(--blue)}

/* hero */
.hero{position:absolute;left:0;top:139px;width:1200px;height:636px;
  background:
   linear-gradient(180deg,rgba(40,50,110,0) 70%,rgba(45,55,120,.55) 100%),
   linear-gradient(100deg,#3c4c92 0%,#4a5aa2 35%,#5b67ab 60%,#6f6aa6 80%,#8a6c9a 100%)}
.hero-title{position:absolute;left:111px;top:186px;font-size:58px;line-height:68px;color:var(--white)}
.hero-text{position:absolute;left:111px;top:326px;width:560px;font-size:20px;line-height:32px;color:#eef}
.btn{position:absolute;display:flex;align-items:center;justify-content:center;background:var(--blue);color:var(--white);font-family:"Audiowide",sans-serif;font-size:15px;border-radius:3px}
.dots{position:absolute;left:574px;top:593px;display:flex;gap:7px}
.dots span{width:12px;height:12px;border-radius:50%;background:#fff}
.dots span.on{background:#f08a3c}

/* about */
.about-title{left:654px;top:826px;font-size:33px}
.about-sub{left:654px;top:870px;font-size:28px;color:var(--blue)}
.about-text{left:654px;top:922px;width:436px;font-size:12.6px;line-height:26px;color:#ddd;text-align:justify}

/* section heads */
.section-head{position:absolute;left:0;width:1200px;text-align:center;font-family:"Audiowide",sans-serif;font-size:40px}
.rule{position:absolute;height:3px;width:55px}
.events-sub{left:0;width:1200px;text-align:center;top:1392px;font-size:16px;color:#eee}
.event-card{position:absolute;top:1451px;width:311px;height:437px;overflow:hidden}
.event-card .meta{position:absolute;left:21px;top:335px;right:21px;font-family:"Rajdhani",sans-serif}
.event-card .date{color:var(--blue);font-size:15px;font-weight:600}
.event-card .title{font-size:16px;line-height:25px;margin-top:8px;font-weight:600}

/* news */
.news{position:absolute;left:0;top:1977px;width:1200px;height:596px;background:var(--bg-alt)}
.news-item{position:absolute;left:645px}
.news-thumb{position:absolute;left:0;top:0;width:133px;height:110px}
.news-meta{position:absolute;left:163px;top:12px;width:280px;font-family:"Rajdhani",sans-serif}
.news-meta .date{color:var(--blue);font-size:15px;font-weight:600}
.news-meta .title{font-size:15px;line-height:26px;font-weight:700;margin-top:6px;letter-spacing:.3px}

/* media */
.media-text{left:111px;top:2808px;width:370px;font-size:13.5px;line-height:27.5px;color:#ddd;text-align:justify}

/* fans */
.fans{position:absolute;left:0;top:3141px;width:1200px;height:409px;
  background:linear-gradient(100deg,#2b95d8 0%,#3aa3e4 40%,#2f9ee1 70%,#2a92d6 100%)}
.fans-text{position:absolute;left:0;top:172px;width:1200px;text-align:center;font-size:16px;line-height:31px;color:#eef6ff}
.btn-outline{position:absolute;left:382px;top:254px;width:436px;height:52px;border:2px solid #fff;border-radius:3px;display:flex;align-items:center;justify-content:center;font-family:"Audiowide",sans-serif;font-size:15px;letter-spacing:1px}

/* partners */
.partner{position:absolute;top:3711px;width:176px;height:101px;border:2px solid #d5d5d5;display:flex;align-items:center;justify-content:center}
.partner-mark{background:#9a9a9a}

/* footer */
.site-footer{position:absolute;left:0;top:3922px;width:1200px;height:339px;background:var(--footer)}
.footer-brand{position:absolute;left:199px;top:90px;display:flex;align-items:center;gap:10px}
.divider{position:absolute;top:58px;width:1px;height:137px;background:var(--line)}
.f-label{font-family:"Rajdhani",sans-serif;font-size:17px;font-weight:600;letter-spacing:.5px}
.f-value{font-family:"Rajdhani",sans-serif;font-size:13px;color:#aaa;line-height:23px}
.social{position:absolute;top:158px;display:flex;align-items:center;gap:6px;font-family:"Rajdhani",sans-serif;font-size:13px;color:#ddd}
.social i{display:block;width:14px;height:14px;border:1.5px solid #fff;border-radius:50%}
.copyright{position:absolute;left:0;top:292px;width:1200px;text-align:center;font-family:"Rajdhani",sans-serif;font-size:15px;color:#ddd}
</style>
</head>
<body>

<header class="site-header">
  <div class="brand"><span class="brand-dot"></span><span class="brand-name">CTG</span></div>
  <div class="contact-item" style="left:733px">
    <div class="contact-icon"><svg width="18" height="18" viewBox="0 0 24 24" fill="none" stroke="#2a9de0" stroke-width="2"><path d="M5 3h4l2 5-3 2a11 11 0 0 0 6 6l2-3 5 2v4a2 2 0 0 1-2 2A18 18 0 0 1 3 5a2 2 0 0 1 2-2z"/></svg></div>
    <div><div class="contact-label">Call Us</div><div class="contact-value">000-484-2290</div></div>
  </div>
  <div class="contact-item" style="left:900px">
    <div class="contact-icon"><svg width="18" height="18" viewBox="0 0 24 24" fill="none" stroke="#2a9de0" stroke-width="2"><rect x="3" y="5" width="18" height="14" rx="1"/><path d="M3 6l9 7 9-7"/></svg></div>
    <div><div class="contact-label">Email</div><div class="contact-value">info@ctg-events.net</div></div>
  </div>
  <nav class="main-nav">
    <a class="active">HOME</a><a>ABOUT CTG</a><a>EVENTS</a><a>NEWS</a><a>MEDIA</a><a>PARTNERS</a><a>POWER RANKINGS</a><a>FANS</a><a>CONTACT</a>
  </nav>
</header>

<section class="hero" role="img" aria-label="Two wrestlers mid-throw in a training hall, tinted blue and violet">
  <h1 class="hero-title display">CORAL TIDE<br>GRAPPLING</h1>
  <p class="hero-text">Sed ut perspiciatis unde omnis iste natus error sit voluptat em accusantium doloremque laudantium</p>
  <div class="btn" style="left:112px;top:410px;width:149px;height:55px">READ MORE</div>
  <div class="dots"><span></span><span class="on"></span><span></span></div>
</section>

<section class="about">
  <div class="photo" role="img" aria-label="Two wrestlers in blue and red singlets facing off in a crouched stance" style="left:63px;top:811px;width:580px;height:430px;border-radius:6px;background:linear-gradient(90deg,#1a2440 0%,#24345e 30%,#2a2d44 50%,#5a2a32 72%,#3a1c22 100%)"></div>
  <h2 class="abs display about-title">ABOUT</h2>
  <h3 class="abs display about-sub">CORAL TIDE GRAPPLING</h3>
  <p class="abs about-text">Sed ut perspiciatis unde omnis iste natus error sit voluptatem accusantium doloremque laudantium, totam rem aperiam, eaque ipsa quae ab inventore veritatis et quasi architecto beatae vitae dicta sunt explicabo. Nemo enim ipsam volup tatem quia voluptas sit aspernatur aut odit aut fugit, sed quia consequuntur magni dolores eos qui ratione voluptatem seq ui nesciunt. Neque porro quisquam est, qui dolorem ipsum quia incidunt ut labore et dolore magnam aliquam quaerat voluptatem.</p>
  <div class="btn" style="left:657px;top:1130px;width:137px;height:48px;font-size:14px">READ MORE</div>
</section>

<section class="events">
  <h2 class="section-head" style="top:1328px;color:var(--blue)">CTG EVENTS</h2>
  <p class="abs events-sub">Sed ut perspiciatis unde omnis iste natus error sit voluptatem accusantium doloremque</p>
  <article class="event-card" style="left:111px">
    <div class="photo" role="img" aria-label="Wrestler in red lifting an opponent in blue in a gym" style="inset:0;background:linear-gradient(180deg,#1d2433 0%,#2e3648 35%,#5a3036 58%,#2a3a6a 72%,#0e1118 88%)"></div>
    <div class="meta"><div class="date">JANUARY 17, 2022</div><div class="title">Sed ut perspiciatis unde omnis iste nat us error sit voluptatem</div></div>
  </article>
  <article class="event-card" style="left:447px">
    <div class="photo" role="img" aria-label="Wrestlers in red and blue locked in a clinch" style="inset:0;background:linear-gradient(180deg,#161a22 0%,#30406e 30%,#2c48a8 50%,#6a2630 66%,#0e1016 88%)"></div>
    <div class="meta"><div class="date">JANUARY 17, 2022</div><div class="title">Sed ut perspiciatis unde omnis iste nat us error sit voluptatem</div></div>
  </article>
  <article class="event-card" style="left:781px">
    <div class="photo" role="img" aria-label="Wrestler lifting an opponent under a warehouse roof" style="inset:0;background:linear-gradient(180deg,#3a3e44 0%,#5b5850 30%,#7a4a40 50%,#4a3a40 68%,#12141a 88%)"></div>
    <div class="meta"><div class="date">JANUARY 17, 2022</div><div class="title">Sed ut perspiciatis unde omnis iste nat us error sit voluptatem</div></div>
  </article>
</section>

<section class="news">
  <div class="photo" role="img" aria-label="Two wrestlers in red and blue grappling on a dark stage" style="left:0;top:0;width:630px;height:596px;background:linear-gradient(160deg,#1c1c28 0%,#3a3a78 30%,#5a2a38 55%,#2a2434 78%,#0b0d12 100%)"></div>
  <h2 class="abs display" style="left:637px;top:55px;font-size:40px;color:var(--blue)">LATEST NEWS</h2>
  <div class="rule" style="left:640px;top:116px;background:var(--blue)"></div>
  <div class="news-item" style="top:154px">
    <div class="news-thumb" role="img" aria-label="Wrestling match on a red mat" style="background:linear-gradient(135deg,#8a3a38,#3a4a80)"></div>
    <div class="news-meta"><div class="date">JANUARY 18, 2021</div><div class="title">SED UT PERSPICIATIS UNDE OMNIS ISTE NATUS ERROR SIT VOLUPTATEM</div></div>
  </div>
  <div class="news-item" style="top:291px">
    <div class="news-thumb" role="img" aria-label="Wrestlers on a blue mat" style="background:linear-gradient(135deg,#5a6070,#3a50a0)"></div>
    <div class="news-meta"><div class="date">JANUARY 18, 2021</div><div class="title">SED UT PERSPICIATIS UNDE OMNIS ISTE NATUS ERROR SIT VOLUPTATEM</div></div>
  </div>
  <div class="news-item" style="top:431px">
    <div class="news-thumb" role="img" aria-label="Wrestlers in red and blue standing bout" style="background:linear-gradient(135deg,#1a2a5a,#6a2a38)"></div>
    <div class="news-meta"><div class="date">JANUARY 18, 2021</div><div class="title">SED UT PERSPICIATIS UNDE OMNIS ISTE NATUS ERROR SIT VOLUPTATEM</div></div>
  </div>
</section>

<section class="media">
  <h2 class="abs display" style="left:111px;top:2716px;font-size:40px;color:var(--blue)">OUR MEDIA</h2>
  <div class="rule" style="left:111px;top:2779px;background:var(--blue)"></div>
  <p class="abs media-text">Sed ut perspiciatis unde omnis iste natus error sit voluptat em accusantium doloremque laudantium, totam rem aperi am, eaque ipsa quae ab illo inventore veritatis et quasi arch itecto beatae vitae dicta sunt explicabo. Nemo enim ipsam voluptatem quia voluptas sit aspernatur aut odit aut fugit, sed omnis iste quia consequuntur magnidolores eos qui ratione omnis iste voluptatem sequi nesciunt.</p>
  <div class="abs" style="left:533px;top:2643px;width:568px;height:402px;border:2px solid var(--blue)"></div>
  <div class="photo" role="img" aria-label="Video still of two wrestlers in headgear on an orange mat" style="left:523px;top:2656px;width:566px;height:402px;background:linear-gradient(180deg,#3a1a1a 0%,#7a2a22 30%,#9a6a5a 50%,#b0502c 72%,#8a3a22 100%)"></div>
  <svg class="abs" style="left:759px;top:2813px" width="90" height="90" viewBox="0 0 90 90"><circle cx="45" cy="45" r="42" fill="none" stroke="#fff" stroke-width="3"/><path d="M36 28 L64 45 L36 62 Z" fill="#fff"/></svg>
</section>

<section class="fans" role="img" aria-label="Blue band with faint wrestling action in the background">
  <h2 class="section-head" style="top:88px">CTG FANS</h2>
  <div class="rule" style="left:572px;top:143px;background:#fff"></div>
  <p class="fans-text">Sed ut perspiciatis unde omnis iste natus error sit voluptatem accusantium doloremque laudantium,<br>totam rem aperiam, eaque ipsa quae ab illo inventore veritatis et quasi architecto</p>
  <div class="btn-outline">HOW TO BECOME PART OF CTG AS A FAN</div>
</section>

<section class="partners">
  <h2 class="section-head" style="top:3603px">OUR PARTNERS</h2>
  <div class="rule" style="left:572px;top:3661px;background:#fff"></div>
  <div class="partner" style="left:111px"><div class="partner-mark" style="width:34px;height:34px;border-radius:50%"></div></div>
  <div class="partner" style="left:311px"><div class="partner-mark" style="width:90px;height:22px"></div></div>
  <div class="partner" style="left:513px"><div class="partner-mark" style="width:30px;height:30px"></div></div>
  <div class="partner" style="left:713px"><div class="partner-mark" style="width:34px;height:34px;border-radius:50%"></div></div>
  <div class="partner" style="left:914px"><div class="partner-mark" style="width:30px;height:30px"></div></div>
</section>

<footer class="site-footer">
  <div class="footer-brand"><span class="brand-dot"></span><span class="brand-name" style="font-size:42px">CTG</span></div>
  <div class="divider" style="left:445px"></div>
  <div class="divider" style="left:776px"></div>
  <svg class="abs" style="left:490px;top:92px" width="18" height="22" viewBox="0 0 18 22" fill="none" stroke="#ccc" stroke-width="1.5"><path d="M9 21s7-7 7-12A7 7 0 0 0 2 9c0 5 7 12 7 12z"/><circle cx="9" cy="9" r="2.5"/></svg>
  <div class="abs" style="left:530px;top:82px">
    <div class="f-label">ADDRESS</div>
    <div class="f-value">#254 Lorem Ipsum Dummy<br>Lorem ipsum</div>
  </div>
  <div class="social" style="left:530px"><i></i>Linkfolk</div>
  <div class="social" style="left:612px"><i></i>Faceboard</div>
  <svg class="abs" style="left:812px;top:92px" width="20" height="20" viewBox="0 0 24 24" fill="none" stroke="#ccc" stroke-width="1.6"><path d="M5 3h4l2 5-3 2a11 11 0 0 0 6 6l2-3 5 2v4a2 2 0 0 1-2 2A18 18 0 0 1 3 5a2 2 0 0 1 2-2z"/></svg>
  <div class="abs" style="left:850px;top:82px"><div class="f-label">PHONE</div><div class="f-value">000.484.2290</div></div>
  <svg class="abs" style="left:812px;top:162px" width="20" height="16" viewBox="0 0 24 18" fill="none" stroke="#ccc" stroke-width="1.6"><rect x="1" y="1" width="22" height="16"/><path d="M1 2l11 8 11-8"/></svg>
  <div class="abs" style="left:852px;top:150px"><div class="f-label">EMAIL</div><div class="f-value">info@ctg-events.net</div></div>
  <p class="copyright">Coral Tide Grappling © 2021.All Rights Reserved.</p>
</footer>

</body>
</html>
```